Agriculture Security Company needs a business card design

We need a business card design for a new company based in Seattle calls Fernwick Guardline LLC. We provide high-end physical security solutions that is geared and focused towards to the marijuana grow operations, wholesalers and distributors. We DO NOT get involved in the retail operations (store fronts). We would like to see designs that incorporate professionalism, reliability, trustworthy and forward thinking as traits of our organization.

Industry/Entity Type

Security

```html
<!DOCTYPE html>
<html lang="en">
<head>
<meta charset="utf-8">
<title>Fernwick Guardline LLC – Business Card</title>
<link rel="stylesheet" href="https://fonts.googleapis.com/css2?family=Crimson+Text:wght@400;600&display=swap">
<style>
  :root {
    --forest: #1f6b32;
    --forest-deep: #155426;
    --olive: #8fae3a;
    --leaf-green: #2e7d3a;
    --white: #ffffff;
    --paper: #f7f8f7;
    --paper-tint: #eef1ee;
    --stage: #e4e5e7;
    --stage-deep: #d3d5d8;
  }
  * { margin: 0; padding: 0; box-sizing: border-box; }
  html, body { width: 1200px; height: 2257px; overflow: hidden; background: var(--white); }
  body { position: relative; font-family: "Crimson Text", Georgia, serif; }

  .panel { position: absolute; left: 42px; width: 1118px; overflow: hidden; }
  .panel--front { top: 37px; height: 680px; }
  .panel--back { top: 751px; height: 683px; background: var(--forest); }
  .panel--pair { top: 1468px; height: 749px; background: radial-gradient(ellipse at 50% 40%, var(--stage) 0%, var(--stage-deep) 100%); }

  /* front */
  .card-front { position: absolute; inset: 0; }
  .card-front__pattern { position: absolute; inset: 0; background: radial-gradient(ellipse at center, var(--paper) 0%, var(--paper-tint) 100%); }
  .wordmark { position: absolute; left: 0; right: 0; top: 50%; transform: translateY(-50%); text-align: center; color: var(--forest); font-weight: 600; line-height: 1; }
  .wordmark__dot { display: inline-block; width: 34px; height: 34px; border-radius: 50%; background: var(--forest); margin-right: 18px; vertical-align: middle; position: relative; top: -10px; }
  .wordmark__name { font-size: 118px; letter-spacing: 2px; text-transform: uppercase; }
  .wordmark__sub { display: block; font-size: 52px; letter-spacing: 4px; text-transform: uppercase; margin-top: 10px; }

  /* back */
  .card-back { position: absolute; inset: 0; background: linear-gradient(160deg, var(--leaf-green) 0%, var(--forest) 55%, var(--forest-deep) 100%); }
  .card-back__leaf { position: absolute; right: 0; top: 0; width: 420px; height: 300px; background: radial-gradient(ellipse at 85% 20%, rgba(20,70,35,0.55) 0%, rgba(20,70,35,0) 70%); }
  .card-back__swoosh { position: absolute; left: 0; top: 0; width: 100%; height: 100%; }
  .contact { position: absolute; left: 168px; top: 146px; color: var(--white); }
  .contact__rule { width: 637px; height: 2px; background: rgba(255,255,255,0.75); }
  .contact__name { font-size: 56px; font-weight: 600; letter-spacing: 1px; line-height: 1; text-transform: uppercase; margin-top: 26px; }
  .contact__role { font-size: 48px; color: var(--olive); line-height: 1; margin-top: 6px; margin-bottom: 20px; }
  .contact__line { font-size: 38px; line-height: 43px; }
  .contact__lines { margin-top: 18px; }
  .contact__web { font-size: 42px; color: var(--olive); letter-spacing: 1px; margin-top: 16px; }

  /* pair */
  .mini { position: absolute; top: 234px; width: 460px; height: 281px; overflow: hidden; box-shadow: 0 14px 28px rgba(0,0,0,0.22); }
  .mini--back { left: 70px; }
  .mini--front { left: 588px; }
  .mini .inner { position: absolute; left: 0; top: 0; width: 1118px; transform: scale(0.4115); transform-origin: 0 0; }
  .mini--back .inner { height: 683px; }
  .mini--front .inner { height: 680px; }
</style>
</head>
<body>

<section class="panel panel--front">
  <div class="card-front">
    <div class="card-front__pattern" role="img" aria-label="Faint repeating leaf pattern background"></div>
    <div class="wordmark">
      <span class="wordmark__dot"></span><span class="wordmark__name">Fernwick</span>
      <span class="wordmark__sub">Guardline LLC</span>
    </div>
  </div>
</section>

<section class="panel panel--back">
  <div class="card-back">
    <div class="card-back__leaf" role="img" aria-label="Soft darker leaf decoration in the corner"></div>
    <svg class="card-back__swoosh" viewBox="0 0 1118 683" preserveAspectRatio="none">
      <path d="M0,478 C220,610 560,590 1118,258 L1118,300 C560,640 220,652 0,528 Z" fill="var(--white)"/>
    </svg>
    <div class="contact">
      <div class="contact__rule"></div>
      <div class="contact__name">Dale Harmon</div>
      <div class="contact__role">Manager</div>
      <div class="contact__rule"></div>
      <div class="contact__lines">
        <div class="contact__line">(555) 014 2290</div>
        <div class="contact__line">dale@fernwick.com</div>
      </div>
      <div class="contact__web">www.fernwick.com</div>
    </div>
  </div>
</section>

<section class="panel panel--pair">
  <div class="mini mini--back">
    <div class="inner">
      <div class="card-back">
        <div class="card-back__leaf" role="img" aria-label="Soft darker leaf decoration in the corner"></div>
        <svg class="card-back__swoosh" viewBox="0 0 1118 683" preserveAspectRatio="none">
          <path d="M0,478 C220,610 560,590 1118,258 L1118,300 C560,640 220,652 0,528 Z" fill="var(--white)"/>
        </svg>
        <div class="contact">
          <div class="contact__rule"></div>
          <div class="contact__name">Dale Harmon</div>
          <div class="contact__role">Manager</div>
          <div class="contact__rule"></div>
          <div class="contact__lines">
            <div class="contact__line">(555) 014 2290</div>
            <div class="contact__line">dale@fernwick.com</div>
          </div>
          <div class="contact__web">www.fernwick.com</div>
        </div>
      </div>
    </div>
  </div>
  <div class="mini mini--front">
    <div class="inner">
      <div class="card-front">
        <div class="card-front__pattern" role="img" aria-label="Faint repeating leaf pattern background"></div>
        <div class="wordmark">
          <span class="wordmark__dot"></span><span class="wordmark__name">Fernwick</span>
          <span class="wordmark__sub">Guardline LLC</span>
        </div>
      </div>
    </div>
  </div>
</section>

</body>
</html>
```